TORVEL Business Card Design

We need a business card design for a current Plastering company now moving to building and constructing new homes.
We have been in the Plastering(rendering) business for 15yrs and have made a good name with our customers for our Top Quality of work that we provide.
We would like TORVEL to be the main attraction with an image of architectural roof tops or house design within it. Blue Yellow and Black are colours we like but are willing to see other ideas.
We would like the design to be modern and communicate quality and experience.
Industry/Entity Type
Building
Contact Information for Business Card
TORVEL Building and Plastering
PO BOX 57390 Marlowe Darwin NT 0815
PH/Fax: 08 89317725 Email: torvel@quellnet.com
Dale: 0417396248 Rosa:0409273516
ABN:58 297 130 846

```html
<!DOCTYPE html>
<html lang="en">
<head>
<meta charset="utf-8">
<title>TORVEL Building and Plastering – Business Cards</title>
<link href="https://fonts.googleapis.com/css2?family=Mulish:wght@300;400;700;800;900&family=Oswald:wght@600&display=swap" rel="stylesheet">
<style>
  :root {
    --navy: #1f2d4b;
    --gold: #d6a52a;
    --gold-line: #e2b63a;
    --paper: #e9ebec;
    --white: #ffffff;
    --ink: #1f2d4b;
    --page: #ffffff;
  }
  * { box-sizing: border-box; margin: 0; padding: 0; }
  html, body { width: 734px; height: 1200px; overflow: hidden; background: var(--page); }
  body { position: relative; font-family: "Mulish", sans-serif; }

  .card {
    position: absolute;
    border-radius: 18px;
    overflow: hidden;
    background: var(--navy);
    box-shadow: 0 6px 14px rgba(0,0,0,0.28);
  }
  .card svg.backdrop { position: absolute; inset: 0; width: 100%; height: 100%; }
  .gold-rule { position: absolute; height: 5px; background: var(--gold-line); }
  .abs { position: absolute; white-space: nowrap; }

  .brand-name {
    font-family: "Mulish", sans-serif; font-weight: 900; color: var(--gold);
    letter-spacing: 1px; display: flex; align-items: center; gap: 10px;
  }
  .brand-mark { width: 14px; height: 14px; background: var(--gold); display: inline-block; }
  .trade-line { font-family: "Oswald", sans-serif; font-weight: 600; color: var(--gold); }

  .contact { color: var(--white); font-weight: 700; font-size: 13px; line-height: 1; }
  .icon { position: absolute; width: 13px; height: 12px; }
  .person { color: var(--ink); font-weight: 300; font-size: 15px; }
  .mobile { color: var(--ink); font-weight: 800; font-size: 15px; }

  /* Card 1 – portrait front */
  .front-portrait { left: 60px; top: 63px; width: 268px; height: 429px; }
  /* Card 2 – portrait back */
  .back-portrait { left: 407px; top: 61px; width: 269px; height: 428px; }
  /* Card 3 – landscape front */
  .front-landscape { left: 169px; top: 549px; width: 427px; height: 266px; }
  /* Card 4 – landscape back */
  .back-landscape { left: 164px; top: 877px; width: 427px; height: 266px; background: var(--white); }
</style>
</head>
<body>

<!-- Portrait front -->
<section class="card front-portrait">
  <svg class="backdrop" viewBox="0 0 268 429" aria-hidden="true">
    <polygon points="0,237 136,154 268,237 268,429 0,429" fill="var(--paper)"/>
  </svg>
  <div class="gold-rule" style="left:0; top:31px; width:268px;"></div>
  <div class="abs brand-name" style="left:0; width:268px; justify-content:center; top:102px; font-size:27px;">TORVEL</div>
  <div class="abs brand-name" style="left:0; width:268px; justify-content:center; top:252px; font-size:30px;"><span class="brand-mark"></span>TORVEL</div>
  <div class="gold-rule" style="left:0; top:303px; width:268px;"></div>
  <div class="abs trade-line" style="left:0; width:268px; text-align:center; top:313px; font-size:21px;">BUILDING &amp; PLASTERING</div>
</section>

<!-- Portrait back -->
<section class="card back-portrait">
  <svg class="backdrop" viewBox="0 0 269 428" aria-hidden="true">
    <polygon points="0,311 136,227 269,311 269,428 0,428" fill="var(--paper)"/>
  </svg>
  <div class="gold-rule" style="left:0; top:30px; width:269px;"></div>
  <div class="abs contact" style="left:67px; top:76px; font-size:12px;">ABN:58 297 130 846</div>

  <svg class="icon" style="left:40px; top:109px;" viewBox="0 0 13 12" aria-hidden="true"><path d="M6.5 1a3.5 3.5 0 0 1 3.5 3.5c0 2.6-3.5 6.5-3.5 6.5S3 7.1 3 4.5A3.5 3.5 0 0 1 6.5 1z" fill="var(--white)"/><circle cx="6.5" cy="4.5" r="1.3" fill="var(--navy)"/></svg>
  <div class="abs contact" style="left:66px; top:109px;">PO BOX 57390</div>
  <div class="abs contact" style="left:66px; top:131px;">Marlowe Darwin NT 0815</div>
  <svg class="icon" style="left:42px; top:151px;" viewBox="0 0 13 12" aria-hidden="true"><rect x="3" y="0.5" width="7" height="4" fill="none" stroke="var(--white)"/><rect x="0.5" y="4.5" width="12" height="5" fill="var(--white)"/><rect x="3" y="8" width="7" height="3.5" fill="var(--navy)" stroke="var(--white)"/></svg>
  <div class="abs contact" style="left:66px; top:152px;">08 89317725</div>
  <svg class="icon" style="left:42px; top:175px;" viewBox="0 0 13 12" aria-hidden="true"><rect x="0.5" y="1.5" width="12" height="9" fill="none" stroke="var(--white)"/><path d="M0.5 1.5l6 5 6-5" fill="none" stroke="var(--white)"/></svg>
  <div class="abs contact" style="left:66px; top:175px;">torvel@quellnet.com</div>

  <div class="abs person" style="left:125px; top:271px;">Dale:</div>
  <svg class="icon" style="left:80px; top:292px;" viewBox="0 0 13 12" aria-hidden="true"><rect x="3" y="0.5" width="7" height="11" rx="1.2" fill="none" stroke="var(--ink)"/></svg>
  <div class="abs mobile" style="left:98px; top:290px;">0417396248</div>
  <div class="abs person" style="left:125px; top:328px;">Rosa:</div>
  <svg class="icon" style="left:80px; top:350px;" viewBox="0 0 13 12" aria-hidden="true"><rect x="3" y="0.5" width="7" height="11" rx="1.2" fill="none" stroke="var(--ink)"/></svg>
  <div class="abs mobile" style="left:98px; top:348px;">0409273516</div>
</section>

<!-- Landscape front -->
<section class="card front-landscape">
  <div class="abs brand-name" style="left:0; width:427px; justify-content:center; top:84px; font-size:34px;"><span class="brand-mark"></span>TORVEL</div>
  <div class="gold-rule" style="left:53px; top:144px; width:312px;"></div>
  <div class="abs brand-name" style="left:0; width:427px; justify-content:center; top:157px; font-size:22px;">TORVEL</div>
  <div class="abs trade-line" style="left:0; width:427px; text-align:center; top:184px; font-size:17px; letter-spacing:1.5px;">BUILDING AND PLASTERING</div>
</section>

<!-- Landscape back -->
<section class="card back-landscape">
  <svg class="backdrop" viewBox="0 0 427 266" aria-hidden="true">
    <rect x="0" y="0" width="427" height="133" fill="var(--navy)"/>
  </svg>
  <div class="gold-rule" style="left:0; top:131px; width:427px; height:4px;"></div>

  <svg class="icon" style="left:56px; top:29px;" viewBox="0 0 13 12" aria-hidden="true"><path d="M6.5 1a3.5 3.5 0 0 1 3.5 3.5c0 2.6-3.5 6.5-3.5 6.5S3 7.1 3 4.5A3.5 3.5 0 0 1 6.5 1z" fill="var(--white)"/><circle cx="6.5" cy="4.5" r="1.3" fill="var(--navy)"/></svg>
  <div class="abs contact" style="left:79px; top:29px;">PO BOX 57390 Marlowe Darwin NT 0815</div>
  <div class="abs contact" style="left:79px; top:51px;">PH/Fax: 08 89317725</div>
  <svg class="icon" style="left:56px; top:73px;" viewBox="0 0 13 12" aria-hidden="true"><rect x="0.5" y="1.5" width="12" height="9" fill="none" stroke="var(--white)"/><path d="M0.5 1.5l6 5 6-5" fill="none" stroke="var(--white)"/></svg>
  <div class="abs contact" style="left:79px; top:73px;">torvel@quellnet.com</div>
  <div class="abs contact" style="left:227px; top:107px;">ABN:58 297 130 846</div>

  <div class="abs person" style="left:76px; top:150px;">Dale:</div>
  <svg class="icon" style="left:57px; top:170px;" viewBox="0 0 13 12" aria-hidden="true"><rect x="3" y="0.5" width="7" height="11" rx="1.2" fill="none" stroke="var(--ink)"/></svg>
  <div class="abs mobile" style="left:75px; top:168px; font-size:14px;">0417396248</div>
  <div class="abs person" style="left:76px; top:205px;">Rosa:</div>
  <svg class="icon" style="left:57px; top:228px;" viewBox="0 0 13 12" aria-hidden="true"><rect x="3" y="0.5" width="7" height="11" rx="1.2" fill="none" stroke="var(--ink)"/></svg>
  <div class="abs mobile" style="left:75px; top:226px; font-size:14px;">0409273516</div>
</section>

</body>
</html>
```